Floorplan brochure design for rental company

We need a brochure designed for our rental company, Bramble Tor Commons.
We have two different categories that we need on this brochure: townhomes (primary) and mobile homes. Size and layout is up to you... choose what you think works best for the information being presented. However, please do not use an odd shape or size; do use a size and format that can be printed by qelvaprint.com.
Font and color choices are up to you. If needed, the fonts from the logo are Americana Extra Bold and BlackJack.
Industry/Entity Type
It Company
Requirements
Must have
- 1. logo and office address/contact information
2. floorplans and prices from attached documents
3. amenities from attached document
Should not have
- Please do not use our website, brambletor.com, as a basis for any design or color scheme decisions. We are working on a redesign of that website with our new logo (attached).

```html
<!DOCTYPE html>
<html lang="en">
<head>
<meta charset="utf-8">
<title>Bramble Tor Commons – Floor Plans</title>
<link href="https://fonts.googleapis.com/css2?family=Lato:wght@400;700&family=Dancing+Script:wght@600;700&display=swap" rel="stylesheet">
<style>
:root{
  --page:#d9d9d9;
  --sky:#6cc6e1;
  --sky-deep:#45b3d9;
  --sea:#1fa2c6;
  --leaf:#4a9b3a;
  --sun:#f6c51b;
  --paper:#e8e8e8;
  --ink:#3b3b3b;
  --teal:#1996c0;
  --plan:#ffffff;
  --plan-line:#c9c9c9;
  --rule:#b8b8b8;
  --white:#ffffff;
}
*{margin:0;padding:0;box-sizing:border-box}
html,body{width:787px;height:1200px;overflow:hidden}
body{background:var(--page);font-family:'Lato',sans-serif;color:var(--ink);position:relative}
.panel{position:absolute;left:37px;width:713px;overflow:hidden}
.outside{top:20px;height:508px;background:var(--sky)}
.inside{top:575px;height:514px;background:var(--paper)}
.panel svg.waves{position:absolute;left:0;top:0}
.abs{position:absolute}
.center{text-align:center;transform:translateX(-50%)}
.nowrap{white-space:nowrap}
.brand{font-weight:700;white-space:nowrap;display:flex;align-items:center;gap:6px}
.brand i{display:inline-block;width:10px;height:10px;border-radius:50%;background:currentColor}
.back-brand{left:171px;top:228px;color:var(--white);font-size:17px}
.back-contact{left:171px;top:266px;color:var(--white);font-size:11px;line-height:1;white-space:nowrap}
.back-contact p{margin-bottom:8px}
.back-contact .invite{font-family:'Dancing Script',cursive;font-size:15px;font-weight:600}
.back-contact .phone{font-size:19px;margin:4px 0 10px}
.front-brand{left:486px;top:176px;color:var(--leaf);font-size:17px}
.title-box{left:399px;top:216px;width:166px;height:37px;background:var(--sun);color:var(--white);font-size:21px;display:flex;align-items:center;justify-content:center;letter-spacing:.5px}
.tagline{left:498px;top:266px;width:240px;color:var(--white);font-family:'Dancing Script',cursive;font-size:16px;line-height:22px;font-weight:600}
.section-title{font-family:'Dancing Script',cursive;color:var(--teal);font-size:31px;font-weight:700;white-space:nowrap}
.inside-brand{left:300px;top:42px;color:var(--leaf);font-size:12px}
.plan-drawing{position:absolute;background:var(--plan);border:1px solid var(--plan-line)}
.plan-name{color:var(--teal);font-size:11px;font-weight:700;letter-spacing:.3px;white-space:nowrap}
.spec{color:var(--teal);font-size:9.5px;line-height:11px;white-space:nowrap}
.price{color:var(--leaf);font-size:21px;line-height:22px;white-space:nowrap}
.price sup{font-size:11px;vertical-align:top;position:relative;top:2px}
.price .or{font-size:9px}
.price.pair{font-size:18px}
.note{font-size:7px;color:var(--ink);white-space:nowrap}
.rule{position:absolute;height:1px;background:var(--rule)}
.offer{left:350px;top:242px;width:102px;min-height:132px;background:var(--leaf);color:var(--white);border-radius:12px 12px 0 0;padding:8px 8px}
.offer h3{font-family:'Dancing Script',cursive;font-size:15px;margin-bottom:3px;white-space:nowrap}
.offer ul{list-style:none;font-size:6.6px;line-height:8px}
.offer li{padding-left:7px;position:relative;margin-bottom:3px}
.offer li::before{content:"›";position:absolute;left:0}
.offer .fine{font-size:6.6px;line-height:8px;margin-top:4px}
.amenities-title{left:25px;top:372px;font-family:'Dancing Script',cursive;color:var(--white);font-size:30px;transform:rotate(-6deg)}
.features-head{left:356px;top:411px;color:var(--white);font-size:10px;letter-spacing:.5px;white-space:nowrap}
.feature-list{color:var(--white);font-size:8.5px;line-height:11px;list-style:none;white-space:nowrap}
.feature-list li{padding-left:9px;position:relative}
.feature-list li::before{content:"›";position:absolute;left:0;font-weight:700}
.feature-list .head{font-weight:700;padding-left:0;font-size:9px}
.feature-list .head::before{content:none}
.feature-list .fine{padding-left:9px;font-size:7.5px}
.feature-list .fine::before{content:none}
.cta{left:389px;top:490px;font-family:'Dancing Script',cursive;color:var(--white);font-size:15px;font-weight:600;white-space:nowrap}
</style>
</head>
<body>

<section class="panel outside">
  <svg class="waves" width="713" height="508" viewBox="0 0 713 508" aria-hidden="true">
    <path d="M600,0 L713,0 L713,508 L470,508 C640,420 700,300 600,0 Z" fill="var(--sky-deep)" opacity=".55"/>
    <path d="M0,424 C220,388 460,360 713,366 L713,508 L0,508 Z" fill="var(--leaf)"/>
    <path d="M0,440 C230,400 470,382 713,392 L713,508 L0,508 Z" fill="var(--sea)"/>
  </svg>

  <div class="abs brand back-brand center"><i></i>Bramble Tor Commons</div>
  <div class="abs back-contact center">
    <p class="invite">Come by our office at</p>
    <p>1870 HARROW LANE, WESTMERE, TX 77014</p>
    <p class="phone">281-555-0148</p>
    <p>www.brambletor.com</p>
  </div>

  <div class="abs brand front-brand center"><i></i>Bramble Tor Commons</div>
  <div class="abs title-box">FLOOR PLANS</div>
  <p class="abs tagline center">Affordable town homes, duplexes, houses, and mobile homes for rent</p>
</section>

<section class="panel inside">
  <svg class="waves" width="713" height="514" viewBox="0 0 713 514" aria-hidden="true">
    <path d="M0,372 C200,366 450,392 713,402 L713,514 L0,514 Z" fill="var(--leaf)"/>
    <path d="M0,426 C240,404 480,404 713,412 L713,514 L0,514 Z" fill="var(--sea)"/>
  </svg>

  <h2 class="abs section-title" style="left:47px;top:14px">Mobile Homes</h2>
  <div class="abs brand inside-brand center"><i></i>Bramble Tor Commons</div>
  <h2 class="abs section-title" style="left:377px;top:24px">Townhomes</h2>

  <!-- Mobile homes -->
  <div class="plan-drawing" style="left:64px;top:71px;width:163px;height:53px" role="img" aria-label="Floor plan 1648, 2 bedroom 1 bath mobile home"></div>
  <div class="abs" style="left:233px;top:76px">
    <div class="spec">16' x 52'<br>2 BR 1 BATH</div>
    <div class="price"><sup>$</sup>750</div>
  </div>
  <div class="abs plan-name" style="left:292px;top:100px">PLAN 1648</div>
  <div class="rule" style="left:45px;top:128px;width:290px"></div>

  <div class="abs" style="left:40px;top:134px">
    <div class="plan-name">PLAN 2762</div>
    <div class="spec" style="margin-left:18px">16' x 76'<br>3 BR 2 BATH</div>
    <div class="price" style="margin-left:18px"><sup>$</sup>850</div>
  </div>
  <div class="plan-drawing" style="left:122px;top:132px;width:198px;height:56px" role="img" aria-label="Floor plan 2762, 3 bedroom 2 bath mobile home"></div>
  <div class="rule" style="left:20px;top:192px;width:315px"></div>

  <div class="plan-drawing" style="left:19px;top:197px;width:222px;height:62px" role="img" aria-label="Floor plan 1887, 3 bedroom 2 bath mobile home"></div>
  <div class="abs" style="left:248px;top:198px">
    <div class="plan-name">PLAN 1887</div>
    <div class="spec" style="margin-left:20px">16' x 76'<br>3 BR 2 BATH</div>
    <div class="price pair"><sup>$</sup>875 <span class="or">or</span> <sup>$</sup>950</div>
    <div class="note" style="margin-left:16px">with 8' x 8' Storage Bldg</div>
  </div>
  <div class="rule" style="left:20px;top:266px;width:315px"></div>

  <div class="abs" style="left:30px;top:274px;width:116px;text-align:right">
    <div class="nowrap"><span class="plan-name">PLAN 105</span>&nbsp;&nbsp;<span class="spec" style="font-size:11px">11' x 35'</span></div>
    <div class="spec">1 BR 1 BATH</div>
    <div class="price"><sup>$</sup>1050</div>
    <div class="note">*Furnished including Utilities</div>
  </div>
  <div class="plan-drawing" style="left:152px;top:275px;width:171px;height:59px" role="img" aria-label="Floor plan 105, 1 bedroom 1 bath mobile home"></div>

  <!-- Townhomes -->
  <div class="plan-drawing" style="left:348px;top:66px;width:137px;height:106px" role="img" aria-label="Floor plan 1132, two story townhome"></div>
  <div class="abs" style="left:356px;top:176px">
    <div class="plan-name">PLAN 1132</div>
    <div class="spec" style="margin-left:22px">2 BR 2.5 BATH<br>2 STORY</div>
    <div class="price" style="margin-left:22px"><sup>$</sup>875</div>
  </div>
  <div class="plan-drawing" style="left:508px;top:66px;width:129px;height:106px" role="img" aria-label="Floor plan 1272, two story townhome"></div>
  <div class="abs" style="left:511px;top:176px">
    <div class="plan-name">PLAN 1272</div>
    <div class="spec" style="margin-left:22px">2 BR 2.5 BATH<br>2 STORY</div>
    <div class="price" style="margin-left:22px"><sup>$</sup>925</div>
  </div>
  <div class="rule" style="left:460px;top:236px;width:218px"></div>

  <div class="abs offer">
    <h3>All units offer:</h3>
    <ul>
      <li>Fenced back yards with concrete patio</li>
      <li>Assigned front door parking</li>
      <li>Ceiling fans in every room</li>
      <li>Dishwasher, microwave, refrigerator &amp; range</li>
      <li>Full-size washer and dryer connections</li>
    </ul>
    <p class="fine">PRICES SUBJECT TO CHANGE WITHOUT NOTICE</p>
  </div>

  <div class="plan-drawing" style="left:463px;top:250px;width:101px;height:138px" role="img" aria-label="Floor plans 1069 and 1070, two bedroom townhome"></div>
  <div class="abs" style="left:569px;top:256px">
    <div class="plan-name">PLAN 1069</div>
    <div class="spec" style="margin-left:22px">2 BR 2.5 BATH</div>
    <div class="price" style="margin-left:22px"><sup>$</sup>875</div>
  </div>
  <div class="rule" style="left:569px;top:312px;width:110px"></div>
  <div class="abs" style="left:569px;top:322px">
    <div class="plan-name">PLAN 1070</div>
    <div class="spec" style="margin-left:22px">2 BR 2.5 BATH<br>COVERED PATIO</div>
    <div class="price" style="margin-left:22px"><sup>$</sup>925</div>
  </div>

  <!-- Amenities -->
  <h2 class="abs amenities-title">Amenities</h2>
  <div class="abs features-head center">OVERALL FEATURES:</div>
  <ul class="abs feature-list" style="left:96px;top:428px">
    <li>Golf Course</li><li>Convenience Store</li><li>Gated Access</li><li>Playground</li><li>Basketball Courts</li><li>Stocked Fishing Lake</li>
  </ul>
  <ul class="abs feature-list" style="left:208px;top:428px">
    <li>Pet Friendly*</li><li>Dog Park</li><li>Extra Storage Available</li><li>Lawn Care Included</li><li>Outdoor Grills Permitted</li><li class="fine">*Breed Restrictions</li>
  </ul>
  <ul class="abs feature-list" style="left:385px;top:428px">
    <li class="head">TOWNHOMES:</li><li>6 Foot Privacy Fenced Backyard</li><li>Concrete Backyard Patio</li><li>Assigned Front Door Parking</li>
  </ul>
  <ul class="abs feature-list" style="left:530px;top:428px">
    <li class="head">MOBILE HOMES:</li><li>Large Fenced Backyard</li><li>Concrete Patio</li><li>Private Driveway</li>
  </ul>
  <p class="abs cta">For more information call 281-555-0148</p>
</section>

</body>
</html>
```